Legislative compliance to home owners, landlords and agents

Logo, business card and stationaly header for a sole trader offering sevices in the UK to home owners, landlords and Letting agents to meet legislation requirement relating to sale and leasing of rental domestic homes. Services offered include Legionella Risk Assessment, Portable Appliance Testing and Energy Performance Certificates. Logo to include depiction of a house and compliance tick list images. Have an existing card with water splash image to reflect water testing, so considering picking up same wave blue. Company name Talvane Property Services. Web www.talvaneps-example.com. email: info@talvaneps-example.com. Address: Glenmorrow, Aberdeen. All three services to be listed. Name as existing card.,

Target Market(s)

UK home owners, landlords, lettings and estate agents

Industry/Entity Type

Property Management

Contact Information for Business Card

Derek Hollingsby CEng, MSoHTF
Address: Glenmorrow, Aberdeen
Web: www.talvaneps-example.com
e-mail info@talvaneps-example.com
Phone: 07921 458 302
Services: Legionella Risk Assessment, Portable Appliance Testing, Energy Performance Certificate

Logo Text

Talvane Property Services

Font styles to use
Sans Serif

Colors

Designer to choose colors to be used in the design.

Requirements
Must have
• Suitable for standard UK business card size 85 mm x 55 mm, with allowance for safety border/ bleed such that colours extend to outside border of card once printed
Nice to have
• Clear font style and layout
• Happy to see images depicting phone, address etc

```html
<!DOCTYPE html>
<html lang="en">
<head>
<meta charset="utf-8">
<title>Talvane Property Services – Business Card</title>
<link href="https://fonts.googleapis.com/css2?family=Alegreya:wght@400;500;700&family=Open+Sans:wght@400;600&display=swap" rel="stylesheet">
<style>
  :root {
    --stage: #262626;
    --card-white: #ffffff;
    --navy: #101a72;
    --wave-blue: #27a8e0;
    --tick-green: #3bb54a;
    --ink: #1c1c1c;
  }
  * { margin: 0; padding: 0; box-sizing: border-box; }
  html, body { width: 1200px; height: 900px; overflow: hidden; background: var(--stage); }
  .stage { position: relative; width: 1200px; height: 900px; }

  .card {
    position: absolute; top: 306px; width: 440px; height: 271px;
    border-radius: 10px; overflow: hidden;
  }
  .card--front { left: 149px; background: var(--card-white); }
  .card--back { left: 608px; background: var(--wave-blue); }

  /* Front */
  .brand-dot {
    position: absolute; left: 150px; top: 22px; width: 44px; height: 44px;
    border-radius: 50%; background: var(--wave-blue);
  }
  .brand-name {
    position: absolute; left: 23px; top: 78px;
    font-family: "Alegreya", serif; font-weight: 500; font-size: 30px;
    color: var(--navy); white-space: nowrap; letter-spacing: 0.2px;
  }
  .holder {
    position: absolute; left: 24px; top: 126px;
    font-family: "Alegreya", serif; color: var(--navy); white-space: nowrap;
  }
  .holder__name { font-weight: 700; font-size: 19px; }
  .holder__creds { font-size: 13px; margin-left: 3px; }

  .contact-list, .service-list {
    position: absolute; top: 165px; list-style: none;
    font-family: "Open Sans", sans-serif; font-size: 12px; color: var(--ink);
  }
  .contact-list { left: 24px; }
  .service-list { left: 226px; }
  .contact-list li, .service-list li {
    display: flex; align-items: center; height: 16px; white-space: nowrap;
  }
  .contact-list svg { width: 9px; height: 9px; margin-right: 6px; fill: var(--navy); }
  .service-list svg { width: 11px; height: 10px; margin-right: 5px; }

  .rule { position: absolute; left: 0; top: 228px; width: 100%; height: 4px; background: var(--navy); }
  .address-band {
    position: absolute; left: 0; top: 231px; width: 100%; height: 40px;
    background: var(--wave-blue); display: flex; align-items: center; justify-content: center;
    font-family: "Open Sans", sans-serif; font-weight: 600; font-size: 12px; color: #fff;
  }

  /* Back */
  .back-texture { position: absolute; inset: 0; background: var(--wave-blue); }
  .back-mark {
    position: absolute; left: 50%; top: 92px; transform: translateX(-50%);
    width: 46px; height: 46px; background: var(--navy);
  }
  .back-name {
    position: absolute; left: 0; width: 100%; top: 148px; text-align: center;
    font-family: "Alegreya", serif; font-weight: 500; font-size: 35px;
    color: var(--navy); white-space: nowrap;
  }
</style>
</head>
<body>
<main class="stage">
  <section class="card card--front" aria-label="Business card front">
    <div class="brand-dot"></div>
    <h1 class="brand-name">Talvane Property Services</h1>
    <p class="holder"><span class="holder__name">Derek Hollingsby</span><span class="holder__creds">CEng, MSoHTF</span></p>

    <ul class="contact-list">
      <li><svg viewBox="0 0 10 10" aria-hidden="true"><path d="M2 0.5l1.8 2-1 1.2c.6 1.3 1.5 2.2 2.8 2.8l1.2-1 2 1.8-1.2 1.7C4.5 8.8 1.2 5.5.3 1.7z"/></svg>07921 458 302</li>
      <li><svg viewBox="0 0 10 10" aria-hidden="true"><path d="M0 2h10v6H0z"/><path d="M0 2l5 3.5L10 2" fill="none" stroke="#fff" stroke-width="1"/></svg>info@talvaneps-example.com</li>
      <li><svg viewBox="0 0 10 10" aria-hidden="true"><circle cx="5" cy="5" r="5"/><path d="M0 5h10M5 0c-2.5 3-2.5 7 0 10M5 0c2.5 3 2.5 7 0 10" fill="none" stroke="#fff" stroke-width=".7"/></svg>www.talvaneps-example.com</li>
    </ul>

    <ul class="service-list">
      <li><svg viewBox="0 0 11 10" aria-hidden="true"><path d="M1 5.5l3 3L10 1.5" fill="none" stroke="var(--tick-green)" stroke-width="2"/></svg>Legionella Risk Assessment</li>
      <li><svg viewBox="0 0 11 10" aria-hidden="true"><path d="M1 5.5l3 3L10 1.5" fill="none" stroke="var(--tick-green)" stroke-width="2"/></svg>Portable Appliance Testing</li>
      <li><svg viewBox="0 0 11 10" aria-hidden="true"><path d="M1 5.5l3 3L10 1.5" fill="none" stroke="var(--tick-green)" stroke-width="2"/></svg>Energy Performance Certificate</li>
    </ul>

    <div class="rule"></div>
    <footer class="address-band">Glenmorrow, Aberdeen</footer>
  </section>

  <section class="card card--back" aria-label="Business card back">
    <div class="back-texture" role="img" aria-label="Faint repeating brand pattern in light blue"></div>
    <div class="back-mark"></div>
    <h2 class="back-name">Talvane Property Services</h2>
  </section>
</main>
</body>
</html>
```